Pebble Lane real estate investment company needs a poster design

We would like a poster design size 18 x 24.
Poster wording -
I WANT TO BUY YOUR ( finish with logo) logo uploaded
website- www.pebblelane-homes.example
phone # 555-217-8843 ( color red for the phone number)
we would like to see the poster on 2 different backgrounds
Yellow background
White background
horizontal

```html
<!DOCTYPE html>
<html lang="en">
<head>
<meta charset="UTF-8">
<title>Pebble Lane – I Want To Buy Your Home</title>
<link rel="stylesheet" href="https://fonts.googleapis.com/css2?family=Luckiest+Guy&family=Montserrat:wght@600;700&display=swap">
<style>
  :root {
    --sun-light: #fbe36e;
    --sun-mid: #f0d24a;
    --sun-deep: #e3c22e;
    --ink: #111111;
    --signal-red: #e41e2b;
    --icon-olive: #a8923a;
  }
  * { margin: 0; padding: 0; box-sizing: border-box; }
  html, body { width: 900px; height: 1200px; overflow: hidden; }
  body { background: var(--sun-mid); }
  .poster {
    position: relative;
    width: 900px;
    height: 1200px;
    overflow: hidden;
    background: linear-gradient(180deg, var(--sun-deep) 0%, var(--sun-light) 42%, var(--sun-mid) 70%, var(--sun-deep) 100%);
  }
  .web-bar {
    position: absolute;
    top: 30px;
    left: 12px;
    right: 12px;
    display: flex;
    align-items: center;
    gap: 12px;
  }
  .web-bar__globe { width: 54px; height: 54px; flex: none; }
  .web-bar__url {
    font-family: "Montserrat", sans-serif;
    font-weight: 700;
    font-size: 38px;
    letter-spacing: 2px;
    color: var(--ink);
    white-space: nowrap;
  }
  .web-bar__cursor {
    position: absolute;
    right: 4px;
    top: 42px;
    width: 56px;
    height: 56px;
  }
  .headline {
    position: absolute;
    left: 0;
    right: 0;
    top: 240px;
    text-align: center;
    font-family: "Luckiest Guy", cursive;
    line-height: 1;
  }
  .headline__line {
    display: block;
    font-size: 112px;
    transform: rotate(-5deg);
    margin-bottom: 22px;
    color: var(--ink);
    text-shadow: 0 4px 8px rgba(0,0,0,0.18);
  }
  .headline__line--accent { color: var(--signal-red); }
  .brand-name {
    position: absolute;
    left: 0;
    right: 0;
    top: 720px;
    text-align: center;
    font-family: "Luckiest Guy", cursive;
    font-size: 118px;
    line-height: 1;
    color: var(--ink);
    white-space: nowrap;
  }
  .phone-line {
    position: absolute;
    left: 0;
    right: 0;
    top: 1112px;
    display: flex;
    justify-content: center;
    align-items: center;
    gap: 18px;
  }
  .phone-line__icon { width: 72px; height: 72px; flex: none; }
  .phone-line__number {
    font-family: "Montserrat", sans-serif;
    font-weight: 700;
    font-size: 64px;
    letter-spacing: 9px;
    color: var(--signal-red);
  }
</style>
</head>
<body>
  <main class="poster">
    <header class="web-bar">
      <svg class="web-bar__globe" viewBox="0 0 54 54" aria-hidden="true">
        <g fill="none" stroke="var(--icon-olive)" stroke-width="3">
          <circle cx="27" cy="27" r="24"/>
          <ellipse cx="27" cy="27" rx="11" ry="24"/>
          <line x1="27" y1="3" x2="27" y2="51"/>
          <line x1="3" y1="27" x2="51" y2="27"/>
          <path d="M7 15 H47 M7 39 H47"/>
        </g>
      </svg>
      <span class="web-bar__url">www.pebblelane-homes.example</span>
      <svg class="web-bar__cursor" viewBox="0 0 56 56" aria-hidden="true">
        <path d="M4 4 L50 24 L32 30 L46 46 L40 52 L26 36 L18 52 Z" fill="none" stroke="var(--icon-olive)" stroke-width="3" stroke-linejoin="round"/>
      </svg>
    </header>

    <h1 class="headline">
      <span class="headline__line">I Want</span>
      <span class="headline__line headline__line--accent">To Buy</span>
      <span class="headline__line">Your</span>
    </h1>

    <p class="brand-name">Pebble Lane</p>

    <footer class="phone-line">
      <svg class="phone-line__icon" viewBox="0 0 72 72" aria-hidden="true">
        <circle cx="36" cy="36" r="32" fill="none" stroke="var(--signal-red)" stroke-width="5"/>
        <path d="M24 18 c3 -2 6 -1 7 2 l3 8 c1 3 0 5 -2 6 l-3 2 c2 6 6 10 12 12 l2 -3 c1 -2 3 -3 6 -2 l8 3 c3 1 4 4 2 7 l-3 4 c-3 3 -8 3 -14 0 c-10 -5 -18 -13 -22 -23 c-2 -6 -2 -11 1 -14 Z" fill="var(--signal-red)"/>
      </svg>
      <span class="phone-line__number">555-217-8843</span>
    </footer>
  </main>
</body>
</html>
```